Mexican construction company needs a business card design

We need a business card design for a company based in Monterrey, Mexico called:

Desarrollos Quilbeta S.A. de C.V.

The company is in the construction business and I would like the businees card to be simple and concise. Please use white background and blue or black text color that say:

"Proyectos de Construcción"-- (Brief description of business)
" Rodrigo Velun Osorio"--- (My name)
"rvelun@correoplat.mx"-- (My email)
"C: (81) 52 19 67 43"-- (My cell)
"O: (81) 56 72 18 94"-- (Office phone)

Please use only the colors of my company that are attached

Please make the back of the business card blue (same blue from logo) and use the logo.

Thanks!

```html
<!DOCTYPE html>
<html lang="es">
<head>
<meta charset="utf-8">
<title>Desarrollos Quilbeta – Tarjeta de presentación</title>
<link rel="stylesheet" href="https://fonts.googleapis.com/css2?family=Barlow:wght@400;500;600&display=swap">
<style>
  :root {
    --navy: #07003d;
    --paper: #ffffff;
    --backdrop: #e9e9ec;
    --ink-grey: #6b6b72;
    --rule: #1d1660;
  }
  * { margin: 0; padding: 0; box-sizing: border-box; }
  html, body {
    width: 1200px; height: 750px; overflow: hidden;
    background: var(--backdrop);
    font-family: "Barlow", Arial, sans-serif;
  }
  .stage { position: relative; width: 1200px; height: 750px; }
  .card {
    position: absolute; left: 371px; width: 462px; height: 263px; overflow: hidden;
  }
  .card--front { top: 129px; background: var(--paper); }
  .card--back { top: 415px; background: var(--navy); }

  .brand-band {
    position: absolute; left: 0; top: 26px; width: 38px; height: 58px; background: var(--navy);
  }
  .brand-mark {
    position: absolute; left: 50px; top: 38px; width: 34px; height: 34px; background: var(--navy);
  }
  .brand-name {
    position: absolute; left: 96px; top: 34px;
    font-weight: 600; font-size: 16px; line-height: 19px; letter-spacing: 1.2px;
    color: var(--navy); text-transform: uppercase;
  }

  .holder-name {
    position: absolute; right: 28px; top: 157px;
    font-weight: 600; font-size: 17px; color: var(--navy); letter-spacing: -0.2px;
  }
  .holder-rule {
    position: absolute; left: 26px; top: 187px; width: 327px; height: 1px; background: var(--rule);
  }
  .holder-title {
    position: absolute; right: 28px; top: 180px;
    font-size: 12px; color: var(--ink-grey);
  }
  .side-tab {
    position: absolute; right: 0; top: 161px; width: 8px; height: 31px; background: var(--navy);
  }

  .contacts { position: absolute; left: 28px; top: 203px; list-style: none; }
  .contacts li {
    display: flex; align-items: center; height: 20px;
    font-size: 12px; color: var(--ink-grey);
  }
  .contacts svg { width: 12px; height: 14px; margin-right: 9px; fill: var(--navy); }
  .email {
    position: absolute; right: 28px; top: 222px; font-size: 11.5px; color: var(--ink-grey);
  }

  .back-brand {
    position: absolute; right: 23px; bottom: 25px; text-align: right; color: var(--paper);
  }
  .back-brand .brand-lines {
    font-weight: 600; font-size: 18px; line-height: 21px; letter-spacing: 1.5px; text-transform: uppercase;
  }
  .back-brand .web {
    margin-top: 3px; font-size: 11px; letter-spacing: 3.6px;
  }
</style>
</head>
<body>
<main class="stage">
  <section class="card card--front" aria-label="Frente de la tarjeta">
    <div class="brand-band"></div>
    <div class="brand-mark"></div>
    <div class="brand-name">Desarrollos<br>Quilbeta</div>

    <div class="holder-name">Rodrigo Velun Osorio</div>
    <div class="holder-rule"></div>
    <div class="holder-title">CEO/Founder</div>
    <div class="side-tab"></div>

    <ul class="contacts">
      <li>
        <svg viewBox="0 0 24 24" aria-hidden="true"><path d="M6.6 10.8c1.4 2.8 3.8 5.1 6.6 6.6l2.2-2.2c.3-.3.7-.4 1-.2 1.1.4 2.3.6 3.6.6.6 0 1 .4 1 1V20c0 .6-.4 1-1 1C10.6 21 3 13.4 3 4c0-.6.4-1 1-1h3.5c.6 0 1 .4 1 1 0 1.3.2 2.5.6 3.6.1.3 0 .7-.2 1z"/></svg>
        (81) 56 72 18 94
      </li>
      <li>
        <svg viewBox="0 0 24 24" aria-hidden="true"><path d="M7 1h10a2 2 0 0 1 2 2v18a2 2 0 0 1-2 2H7a2 2 0 0 1-2-2V3a2 2 0 0 1 2-2zm0 3v14h10V4z"/></svg>
        (81) 52 19 67 43
      </li>
    </ul>
    <div class="email">rvelun@correoplat.mx</div>
  </section>

  <section class="card card--back" aria-label="Reverso de la tarjeta">
    <div class="back-brand">
      <div class="brand-lines">Desarrollos<br>Quilbeta</div>
      <div class="web">www.quilbeta.mx</div>
    </div>
  </section>
</main>
</body>
</html>
```